Tarrowby Builders Business Card Design

We require a business Card for a new Building Company called Tarrowby Builders. We are General Builders that specialize in Industrial, Commercial and Domestic building work. We would like to see a design that incorporates Blue ,Red and White as the colour scheme and a design that will highlight a building theme.
(Once this design is achieved will need to incorporate this for the other side of the business which is Tarrowby Joinery )

Contact Information for Business Card

TARROWBY BUILDERS
17 Wendaree Rd Nuriootpa SA 5355
Mobile 0427390548
Telephone 08 85047316
Marcus Delroy
Director / Supervisor

```html
<!DOCTYPE html>
<html lang="en">
<head>
<meta charset="utf-8">
<title>Tarrowby Builders – Business Card</title>
<link href="https://fonts.googleapis.com/css2?family=Barlow:wght@400;500;600;700&display=swap" rel="stylesheet">
<style>
  :root{
    --navy:#17104b;
    --red:#e31b23;
    --red-dark:#b3141b;
    --white:#ffffff;
    --charcoal:#2f2f31;
    --ink:#444447;
    --backdrop:#2b2538;
  }
  *{margin:0;padding:0;box-sizing:border-box}
  html,body{width:1200px;height:800px;overflow:hidden;background:var(--backdrop);font-family:"Barlow",sans-serif}
  .sheet{position:relative;width:1200px;height:800px}
  .card{position:absolute;top:235px;width:540px;height:330px;overflow:hidden;box-shadow:0 18px 40px rgba(0,0,0,.45)}
  .card--front{left:40px}
  .card--back{left:620px}
  .card__shapes{position:absolute;inset:0;width:540px;height:330px;display:block}

  /* front */
  .brand{position:absolute;left:0;right:0;top:112px;display:flex;justify-content:center;align-items:center;gap:10px}
  .brand__mark{width:18px;height:18px;background:var(--white)}
  .brand__name{color:var(--white);font-weight:600;font-size:23px;letter-spacing:.5px;white-space:nowrap}
  .website{position:absolute;left:120px;width:300px;top:240px;text-align:center;color:var(--white);font-size:11px;font-weight:500;letter-spacing:3px;white-space:nowrap}

  /* back */
  .contact{position:absolute;left:92px;color:var(--ink);font-size:15px;line-height:19px;font-weight:500;white-space:nowrap}
  .contact--phone{top:78px}
  .contact--web{top:150px}
  .contact--address{top:218px}
  .person{position:absolute;left:330px;top:128px;color:var(--white);white-space:nowrap}
  .person__name{font-size:31px;font-weight:700;line-height:1}
  .person__role{font-size:14px;font-weight:500;letter-spacing:1.5px;margin-top:8px}
</style>
</head>
<body>
<main class="sheet">

  <section class="card card--front" aria-label="Card front">
    <svg class="card__shapes" viewBox="0 0 540 330" aria-hidden="true">
      <rect width="540" height="330" fill="var(--navy)"/>
      <line x1="20" y1="128" x2="150" y2="128" stroke="var(--red)" stroke-width="1.5"/>
      <line x1="390" y1="128" x2="520" y2="128" stroke="var(--red)" stroke-width="1.5"/>
      <rect y="215" width="540" height="115" fill="var(--red)"/>
      <path d="M130 222 Q135 208 150 208 L390 208 Q402 208 408 222 L440 282 L100 282 Z" fill="var(--red-dark)"/>
    </svg>
    <div class="brand">
      <span class="brand__mark"></span>
      <span class="brand__name">Tarrowby Builders</span>
    </div>
    <p class="website">WWW.TARROWBYBUILDERS.COM</p>
  </section>

  <section class="card card--back" aria-label="Card back">
    <svg class="card__shapes" viewBox="0 0 540 330" aria-hidden="true">
      <rect width="540" height="330" fill="var(--white)"/>
      <rect width="46" height="330" fill="var(--charcoal)"/>
      <circle cx="46" cy="90" r="22" fill="var(--charcoal)"/>
      <circle cx="46" cy="160" r="22" fill="var(--charcoal)"/>
      <circle cx="46" cy="228" r="22" fill="var(--charcoal)"/>
      <path d="M42 80 q-4 0 -4 5 q1 10 12 15 q4 1 5 -3 l-4 -3 l-3 2 q-4 -2 -5 -6 l2 -3 z" fill="var(--white)"/>
      <g fill="none" stroke="var(--white)" stroke-width="1.6">
        <circle cx="48" cy="160" r="9"/>
        <ellipse cx="48" cy="160" rx="4" ry="9"/>
        <line x1="39" y1="160" x2="57" y2="160"/>
      </g>
      <path d="M48 238 q-9 -9 -9 -14 a9 9 0 0 1 18 0 q0 5 -9 14 z" fill="var(--white)"/>
      <circle cx="48" cy="224" r="3.2" fill="var(--charcoal)"/>
      <path d="M300 0 L540 0 L540 330 L222 330 Q236 150 300 0 Z" fill="var(--red)"/>
      <path d="M328 0 L540 0 L540 330 L250 330 Q264 150 328 0 Z" fill="var(--navy)"/>
      <line x1="318" y1="255" x2="490" y2="255" stroke="var(--red)" stroke-width="1.5"/>
    </svg>
    <p class="contact contact--phone">Mobile 0427390548<br>Telephone 08 85047316</p>
    <p class="contact contact--web">xxxxxx@xxxx.xx<br>xxx.xxxxxxxx.com</p>
    <p class="contact contact--address">17 Wendaree Rd,<br>Kellbrook SA 5371</p>
    <div class="person">
      <p class="person__name">Marcus Delroy</p>
      <p class="person__role">Director / Supervisor</p>
    </div>
  </section>

</main>
</body>
</html>
```